Harbor Ridge Casting business card
Derek Halloway
Project: Harbor Ridge Casting business card
Harbor Ridge Casting business card - Manufacturing
Creative Brief
Simple
4307 Tilden Street Irvine, CA 92618
949-617-4380 x35
derek@harborridgecasting.com
www.harborridgecasting.com

```html
<!DOCTYPE html>
<html lang="en">
<head>
<meta charset="utf-8">
<title>Harbor Ridge Casting business card</title>
<link href="https://fonts.googleapis.com/css2?family=Open+Sans:wght@400;600;700&display=swap" rel="stylesheet">
<style>
  :root {
    --bg: #d9d9d9;
    --card-white: #ffffff;
    --orange: #e8783c;
    --orange-light: #f08a4f;
    --navy: #1f4a8c;
    --grey: #6b6b6b;
  }
  html, body {
    margin: 0;
    padding: 0;
    width: 1200px;
    height: 902px;
    overflow: hidden;
    background: var(--bg);
    font-family: "Open Sans", Arial, sans-serif;
  }
  .canvas {
    position: relative;
    width: 1200px;
    height: 902px;
  }
  .card {
    position: absolute;
    width: 560px;
    height: 320px;
    box-shadow: 0 10px 24px rgba(0,0,0,0.18);
    box-sizing: border-box;
  }
  .card-back {
    left: 150px;
    top: 100px;
    background: radial-gradient(circle at 45% 55%, var(--orange-light), var(--orange) 75%);
    display: flex;
    align-items: center;
    justify-content: center;
  }
  .card-back .web {
    color: #fff;
    font-size: 17px;
    letter-spacing: 3px;
  }
  .card-front {
    left: 490px;
    top: 480px;
    background: var(--card-white);
  }
  .holder {
    position: absolute;
    right: 80px;
    top: 46px;
    text-align: right;
  }
  .holder .name {
    color: var(--orange);
    font-weight: 700;
    font-size: 19px;
    margin: 0;
  }
  .holder .title {
    color: var(--grey);
    font-size: 15px;
    margin: 2px 0 0;
  }
  .front-web {
    position: absolute;
    right: 30px;
    top: 150px;
    color: var(--orange);
    font-size: 12px;
    letter-spacing: 2px;
  }
  .brand {
    position: absolute;
    left: 30px;
    top: 122px;
    display: flex;
    align-items: center;
    gap: 10px;
  }
  .brand-dot {
    width: 34px;
    height: 34px;
    border-radius: 50%;
    background: var(--orange);
    flex: none;
  }
  .brand-name {
    color: var(--navy);
    font-weight: 700;
    font-size: 20px;
    line-height: 1;
    margin: 0;
  }
  .contact {
    position: absolute;
    left: 30px;
    bottom: 28px;
    list-style: none;
    margin: 0;
    padding: 0;
    color: var(--grey);
    font-size: 11px;
  }
  .contact li {
    display: flex;
    align-items: center;
    gap: 7px;
    margin-top: 4px;
  }
  .contact svg {
    width: 10px;
    height: 10px;
    fill: var(--orange);
    flex: none;
  }
</style>
</head>
<body>
<div class="canvas">
  <section class="card card-back">
    <span class="web">www.harborridgecasting.com</span>
  </section>

  <section class="card card-front">
    <div class="holder">
      <p class="name">Derek Halloway</p>
      <p class="title">Owner</p>
    </div>

    <span class="front-web">www.harborridgecasting.com</span>

    <div class="brand">
      <span class="brand-dot"></span>
      <p class="brand-name">Harbor Ridge Casting</p>
    </div>

    <ul class="contact">
      <li>
        <svg viewBox="0 0 10 10" aria-hidden="true"><path d="M2 0.5 L3.8 2.6 L2.9 3.6 C3.5 5 4.8 6.3 6.3 7 L7.3 6.1 L9.5 8 L8.2 9.5 C4.5 9 1 5.5 0.5 1.8 Z"/></svg>
        949-617-4380 x35
      </li>
      <li>
        <svg viewBox="0 0 10 10" aria-hidden="true"><rect x="0.5" y="2" width="9" height="6.5"/><path d="M0.5 2 L5 5.5 L9.5 2" fill="none" stroke="#fff" stroke-width="0.8"/></svg>
        derek@harborridgecasting.com
      </li>
      <li>
        <svg viewBox="0 0 10 10" aria-hidden="true"><path d="M5 0.5 C2.8 0.5 1.6 2.1 1.6 3.8 C1.6 6.2 5 9.5 5 9.5 C5 9.5 8.4 6.2 8.4 3.8 C8.4 2.1 7.2 0.5 5 0.5 Z"/><circle cx="5" cy="3.8" r="1.3" fill="#fff"/></svg>
        4307 Tilden Street Irvine, CA 92618
      </li>
    </ul>
  </section>
</div>
</body>
</html>
```